Watch brand needs new business cards

Fernhollow Clock Company are looking for a new business card design incorporating our logo and brand colours as per our website.

Design should be 90x55mm with 3mm print margin from edges and 3mm external bleed.

Card should be double sided, e.g. logo one side, personal details on the other.

Logo will be provided as a vector.

The card must be able to show:
- Staff name
- Position
- Office Address
- Email
- Telephone number
- Website address

Final work must be provided in an editable format to allow us to add staff details (e.g. an AI or PSD file).

Industry/Entity Type

Business

```html
<!DOCTYPE html>
<html lang="en">
<head>
<meta charset="utf-8">
<title>Fernhollow Clock Company – Business Cards</title>
<link rel="stylesheet" href="https://fonts.googleapis.com/css2?family=Cinzel:wght@600&family=Oswald:wght@600&family=Open+Sans:wght@400&display=swap">
<style>
  :root {
    --backdrop: #5b5b5b;
    --card-dark: #0b0b0b;
    --card-dark-sheen: #262626;
    --card-light: #ffffff;
    --ink: #111111;
    --ink-soft: #7a7a7a;
    --paper-white: #ffffff;
  }
  * { margin: 0; padding: 0; box-sizing: border-box; }
  html, body {
    width: 1200px; height: 1000px; overflow: hidden;
    background: var(--backdrop);
  }
  .canvas { position: relative; width: 1200px; height: 1000px; }

  .card { position: absolute; left: 220px; width: 760px; }

  /* Front */
  .card-front {
    top: 50px; height: 433px;
    background: linear-gradient(118deg, var(--card-dark) 0%, var(--card-dark) 55%, var(--card-dark-sheen) 75%, var(--card-dark) 100%);
    color: var(--paper-white);
  }
  .front-mark {
    position: absolute; left: 320px; top: 108px;
    width: 120px; height: 120px; border-radius: 50%;
    border: 6px solid var(--paper-white);
  }
  .front-name {
    position: absolute; left: 0; right: 0; top: 240px;
    text-align: center;
    font-family: 'Cinzel', Georgia, serif; font-weight: 600;
    color: var(--paper-white);
  }
  .front-name-main {
    display: block;
    font-size: 54px; line-height: 64px; letter-spacing: 1px;
  }
  .front-name-sub {
    display: block;
    font-size: 19px; line-height: 24px; letter-spacing: 3px;
    margin-top: -2px;
  }

  /* Back */
  .card-back {
    top: 523px; height: 437px;
    background: var(--card-light); color: var(--ink);
  }
  .spine {
    position: absolute; left: 51px; top: 0; bottom: 0;
    width: 2px; background: var(--ink);
  }
  .staff-name {
    position: absolute; left: 68px; top: 38px;
    font-family: 'Oswald', 'Arial Narrow', sans-serif; font-weight: 600;
    font-size: 32px; line-height: 1.1; color: var(--ink);
  }
  .staff-role {
    position: absolute; left: 68px; top: 78px;
    font-family: 'Open Sans', Arial, sans-serif;
    font-size: 15px; color: var(--ink-soft);
  }
  .contact {
    position: absolute; left: 40px;
    font-family: 'Open Sans', Arial, sans-serif;
    font-size: 15px; line-height: 22px; color: var(--ink-soft);
    list-style: none;
  }
  .contact li { display: flex; align-items: flex-start; }
  .contact svg { flex: none; width: 20px; height: 20px; margin: 1px 8px 0 0; }
  .contact-address { top: 276px; }
  .contact-lines { top: 333px; }
  .contact-lines li { height: 21px; }
  .back-mark {
    position: absolute; left: 540px; top: 46px;
    width: 176px; height: 176px; border-radius: 50%;
    border: 8px solid var(--ink);
  }
  .back-name {
    position: absolute; left: 528px; width: 200px; top: 234px;
    text-align: center;
    font-family: 'Oswald', 'Arial Narrow', sans-serif; font-weight: 600;
    font-size: 15px; line-height: 19px; letter-spacing: 1px; color: var(--ink);
  }
</style>
</head>
<body>
<main class="canvas">

  <section class="card card-front" aria-label="Card front">
    <div class="front-mark" aria-hidden="true"></div>
    <p class="front-name">
      <span class="front-name-main">FERNHOLLOW</span>
      <span class="front-name-sub">CLOCK COMPANY</span>
    </p>
  </section>

  <section class="card card-back" aria-label="Card back">
    <div class="spine"></div>
    <h1 class="staff-name">OWEN HARTLEY</h1>
    <p class="staff-role">Founder &amp; CEO</p>

    <ul class="contact contact-address">
      <li>
        <svg viewBox="0 0 20 20" aria-hidden="true"><circle cx="10" cy="10" r="9" fill="var(--ink)"/><path d="M10 4.5a3.5 3.5 0 0 0-3.5 3.5c0 2.6 3.5 6.5 3.5 6.5s3.5-3.9 3.5-6.5A3.5 3.5 0 0 0 10 4.5z" fill="var(--paper-white)"/><circle cx="10" cy="8" r="1.3" fill="var(--ink)"/></svg>
        <span>Street name, Suite 100,<br>State, Zip Code, Country</span>
      </li>
    </ul>

    <ul class="contact contact-lines">
      <li>
        <svg viewBox="0 0 20 20" aria-hidden="true"><circle cx="10" cy="10" r="9" fill="var(--ink)"/><path d="M7 5.5l1.8 2.2-1 1.2a6 6 0 0 0 3.3 3.3l1.2-1 2.2 1.8-1.2 1.5C9.6 14.5 5.5 10.4 5.5 6.7z" fill="var(--paper-white)"/></svg>
        <span>012-345-6789</span>
      </li>
      <li>
        <svg viewBox="0 0 20 20" aria-hidden="true"><circle cx="10" cy="10" r="9" fill="var(--ink)"/><rect x="5" y="6.5" width="10" height="7" fill="var(--paper-white)"/><path d="M5 6.5l5 4 5-4" fill="none" stroke="var(--ink)" stroke-width="1"/></svg>
        <span>info@youremail.com</span>
      </li>
      <li>
        <svg viewBox="0 0 20 20" aria-hidden="true"><circle cx="10" cy="10" r="9" fill="var(--ink)"/><g fill="none" stroke="var(--paper-white)" stroke-width="1"><circle cx="10" cy="10" r="5"/><ellipse cx="10" cy="10" rx="2.2" ry="5"/><path d="M5 10h10"/></g></svg>
        <span>www.yourwebsite.com</span>
      </li>
    </ul>

    <div class="back-mark" aria-hidden="true"></div>
    <p class="back-name">FERNHOLLOW<br>CLOCK COMPANY</p>
  </section>

</main>
</body>
</html>
```